Polish brewery needs BEER LABEL design for WEDDINGS

We need beer label design for weddings. Our brewery is located on South of Poland and it is called Zakład Wrzos [PL]/Heather Works [ENG]. We feel strong connection to mountains and we use water from the mountain in our vicinity.
Regarding beer style it is India Pale Ale so beer is bitter and aromatic because of high addition of hops. Label design has to be modern and simple. We would prefer bright and cream colors.
We need to have opportunity to edit data which are on the label so we will need to get appropriate files.
In attached files you can find all details. If any additional information will be required please do not hesitate and contact with me.

Target Market(s)

Weddings

Font styles to use
Sans Serif
Script

Colors
ffffff

Requirements
Must have
• Information listed in documents in attached files
Nice to have
• Some nice graphics
Bright and cream colors.
Should not have
• -

```html
<!DOCTYPE html>
<html lang="pl">
<head>
<meta charset="utf-8">
<title>Julian &amp; Alina – India Pale Ale – etykieta</title>
<link rel="stylesheet" href="https://fonts.googleapis.com/css2?family=Arimo:wght@400;700&family=Montserrat:wght@500;600;700&family=Pinyon+Script&family=Libre+Baskerville&family=Crimson+Text:ital@1&display=swap">
<style>
  :root {
    --cream: #f3e6d9;
    --page: #ffffff;
    --ink: #2a2526;
    --brown: #6e3a33;
    --coral: #d88a6f;
    --gold: #9b7b3d;
    --hop: #c9a79a;
  }
  * { box-sizing: border-box; margin: 0; padding: 0; }
  html, body { width: 927px; height: 1200px; overflow: hidden; background: var(--page); }
  .canvas { position: relative; width: 927px; height: 1200px; }
  .label {
    position: absolute; left: 20px; top: 403px;
    width: 1610px; height: 715px;
    background: var(--cream);
    transform: scale(0.551); transform-origin: top left;
    color: var(--ink);
    font-family: "Arimo", Arial, sans-serif;
    overflow: hidden;
  }
  .panel { position: absolute; top: 0; height: 715px; }
  .panel-info { left: 0; width: 538px; }
  .panel-front { left: 538px; width: 537px; border-left: 2px solid var(--ink); border-right: 2px solid var(--ink); }
  .panel-story { left: 1075px; width: 535px; }
  .abs { position: absolute; }

  /* info panel */
  .ingredients { left: 25px; top: 33px; width: 489px; height: 149px; background: var(--ink); border-radius: 10px; color: #fff; text-align: center; }
  .ingredients h2 { font-family: "Montserrat", sans-serif; font-weight: 700; font-size: 30px; letter-spacing: 1px; margin-top: 12px; }
  .ingredients .rule { width: 140px; height: 2px; background: var(--coral); margin: 6px auto 14px; }
  .ingredients p { font-size: 24px; line-height: 29px; }
  .ingredients u { text-underline-offset: 3px; }
  .info-heading { font-size: 31px; font-weight: 700; left: 24px; }
  .info-text { font-size: 26px; line-height: 32px; left: 26px; }
  .batch-box { left: 28px; top: 283px; width: 336px; height: 42px; border: 2px solid var(--ink); }
  .brand-box { left: 50px; top: 537px; width: 427px; height: 155px; border: 1.5px solid var(--ink); padding: 16px 0 0 28px; }
  .brand-name { font-family: "Arimo", sans-serif; color: var(--gold); font-size: 26px; line-height: 28px; font-weight: 400; }
  .brand-addr { font-size: 14px; line-height: 18px; margin-top: 8px; }
  .brand-made { font-size: 13px; line-height: 18px; margin-top: 12px; }
  .brand-square { right: 46px; top: 48px; width: 52px; height: 52px; background: var(--gold); }

  /* front panel */
  .deco { background: var(--hop); opacity: .55; border-radius: 40px; }
  .deco-sprig { background: var(--ink); opacity: .25; border-radius: 10px; }
  .couple { left: 0; width: 100%; top: 30px; text-align: center; font-family: "Pinyon Script", cursive; font-weight: 400; line-height: 1; }
  .couple .name { display: block; font-size: 118px; line-height: 120px; }
  .couple .name-1 { padding-right: 30px; }
  .couple .amp { display: block; font-size: 88px; line-height: 80px; padding-left: 20px; }
  .couple .name-2 { padding-left: 70px; }
  .date { left: 0; width: 100%; top: 405px; text-align: center; font-family: "Libre Baskerville", serif; font-size: 24px; letter-spacing: 4px; }
  .coral-rule { height: 2px; background: var(--coral); }
  .front-rule { left: 212px; width: 112px; }
  .wish { left: 0; width: 100%; top: 496px; text-align: center; font-family: "Crimson Text", serif; font-style: italic; font-size: 21px; line-height: 27px; }
  .style-name { left: 0; width: 100%; top: 620px; text-align: center; font-family: "Pinyon Script", cursive; font-size: 52px; }

  /* story panel */
  .flourish { left: 46px; top: 45px; width: 432px; height: 24px; background: linear-gradient(90deg, transparent, var(--brown) 20%, var(--brown) 80%, transparent); opacity: .35; border-radius: 12px; }
  .story { left: 46px; top: 110px; width: 433px; font-size: 20px; line-height: 32px; text-align: justify; text-align-last: justify; }
  .story span { display: block; }
  .stat { width: 104px; text-align: center; font-family: "Montserrat", sans-serif; color: var(--brown); }
  .stat .ring { width: 104px; height: 104px; border: 3px solid var(--brown); border-radius: 50%; display: flex; align-items: center; justify-content: center; font-size: 26px; font-weight: 600; }
  .stat .icon { width: 62px; height: 40px; border-radius: 20px; background: var(--hop); opacity: .7; }
  .stat .caption { font-size: 17px; font-weight: 600; letter-spacing: 1px; margin-top: 6px; }
  .story-rule { left: 205px; top: 655px; width: 120px; }
  .socials { left: 18px; top: 668px; width: 505px; display: flex; justify-content: space-between; align-items: center; font-family: "Montserrat", sans-serif; font-weight: 700; font-size: 15px; }
  .social { display: flex; align-items: center; gap: 6px; white-space: nowrap; }
  .social .dot { width: 34px; height: 34px; border-radius: 50%; background: var(--ink); flex: none; }
</style>
</head>
<body>
<div class="canvas">
  <div class="label">

    <section class="panel panel-info">
      <div class="abs ingredients">
        <h2>SKŁADNIKI</h2>
        <div class="rule"></div>
        <p>woda, <u>słód jęczmienny</u>, chmiel,<br>liście limonki, drożdże</p>
      </div>
      <h3 class="abs info-heading" style="top:207px">DATA PRZYDATNOŚCI:</h3>
      <p class="abs info-text" style="top:240px">Data stanowi numer partii</p>
      <div class="abs batch-box"></div>
      <p class="abs info-text" style="top:343px">Należy przechowywać w<br>suchym i ciemnym miejscu.</p>
      <h3 class="abs info-heading" style="top:437px">OBJĘTOŚĆ BUTELKI:</h3>
      <p class="abs info-text" style="top:469px">330ml</p>
      <div class="abs brand-box">
        <div class="brand-name">Zakład Wrzos</div>
        <div class="brand-addr">Zielona Dolina 12, 34-100 Zielona Dolina</div>
        <div class="brand-made">Miejsce warzenia i rozlewu piwa:<br>Browar Pod Jodłą<br>Jodłowa 45, 34-200 Jodłowa</div>
        <div class="abs brand-square"></div>
      </div>
    </section>

    <section class="panel panel-front">
      <div class="abs deco" style="right:0;top:0;width:205px;height:110px" role="img" aria-label="Rysunek szyszek chmielu w narożniku"></div>
      <div class="abs deco" style="left:0;top:40px;width:55px;height:200px" role="img" aria-label="Rysunek szyszek chmielu przy krawędzi"></div>
      <div class="abs deco-sprig" style="right:20px;top:160px;width:30px;height:110px" role="img" aria-label="Gałązka ozdobna"></div>
      <div class="abs deco-sprig" style="left:28px;top:430px;width:36px;height:120px" role="img" aria-label="Gałązka ozdobna"></div>
      <div class="abs deco-sprig" style="right:30px;top:625px;width:16px;height:60px" role="img" aria-label="Gałązka ozdobna"></div>
      <h1 class="abs couple">
        <span class="name name-1">Julian</span>
        <span class="amp">&amp;</span>
        <span class="name name-2">Alina</span>
      </h1>
      <p class="abs date">03.12.16</p>
      <div class="abs coral-rule front-rule" style="top:470px"></div>
      <p class="abs wish">Lorem ipsum dolor sit amet, consectetur<br>adipiscing elit, sed do eiusmod tempor<br>incididunt ut labore et dolore magna aliqua.</p>
      <div class="abs coral-rule front-rule" style="top:600px"></div>
      <p class="abs style-name">India Pale Ale</p>
    </section>

    <section class="panel panel-story">
      <div class="abs flourish" role="img" aria-label="Ozdobny ornament rozdzielający"></div>
      <p class="abs story">
        <span>Trzymasz w ręku naszą autorską IPA do</span>
        <span>produkcji której wykorzystujemy wodę</span>
        <span>wypływającą z samego serca Beskidu</span>
        <span>Wysokiego – Babiej Góry. IPA lubi chmiele i</span>
        <span>goryczkę, ale żeby nie było nudno</span>
        <span>postanowiliśmy ją wzbogacić limonką.</span>
      </p>
      <div class="abs stat" style="left:110px;top:336px"><div class="ring">5,5%</div><div class="caption">ALK</div></div>
      <div class="abs stat" style="left:247px;top:336px"><div class="ring"><div class="icon" role="img" aria-label="Ikona chmielu – goryczka"></div></div><div class="caption">IBU</div></div>
      <div class="abs stat" style="left:386px;top:336px"><div class="ring"><div class="icon" role="img" aria-label="Ikona kłosów – barwa"></div></div><div class="caption">EBC</div></div>
      <div class="abs stat" style="left:172px;top:486px"><div class="ring">14%</div><div class="caption">EXT</div></div>
      <div class="abs stat" style="left:317px;top:486px"><div class="ring"><div class="icon" role="img" aria-label="Ikona kropli wody z górami"></div></div><div class="caption">WODA</div></div>
      <div class="abs coral-rule story-rule"></div>
      <div class="abs socials">
        <div class="social"><span class="dot"></span>zakladwrzos</div>
        <div class="social"><span class="dot"></span>zaklad.wrzos</div>
        <div class="social"><span class="dot"></span>www.zakladwrzos.pl</div>
      </div>
    </section>

  </div>
</div>
</body>
</html>
```